Business Card Design Project

We have a logo, but would like to expand the use of it into a business card design. We are a B2B technology exchange platform for institutional investors to invest excess cash into short term assets matching their credit and pricing parameters. The assets are fractionalized and investors invest in portions.

Our customers are large, institutional, financial companies who are a bit traditional. We are high energy rebels with a cause...we are a disruptive technology and want to be viewed as a game changer but we need to present an image of trustworthiness and secure.

We are open not only to the image design but the material, die cut, etc. but want to stay in the traditional size of a business card.

We have other formats of the logo if needed. Our website is www.brambleharbor.com

I have posted a powerpoint template that we have been using.  This should not be considered the template we will use (after business cards we will have another project to incorporate business card design into powerpoint template) but just to give you a flavor of where we have been and have used in the past.

Target Market(s)

Institutional investors, asset managers, large fund institutions

Industry/Entity Type

Financial

Requirements
Must have
• Our logo
Traditional size
Nice to have
• unique use of logo, unique material, die cut, etc
Crisp, clean look
Use of both sides of card in a creative manner

```html
<!DOCTYPE html>
<html lang="en">
<head>
<meta charset="utf-8">
<title>Bramble Harbor — Business Card</title>
<link href="https://fonts.googleapis.com/css2?family=Montserrat:wght@400;600;700&display=swap" rel="stylesheet">
<style>
  :root {
    --backdrop: #e6e6ea;
    --card-dark: #5f5f60;
    --card-light: #f7f8fa;
    --ink-dark: #58585a;
    --ink-light: #ffffff;
    --accent: #e8900f;
    --deco-on-dark: #727273;
    --deco-on-light: #e3e5e8;
  }
  * { box-sizing: border-box; margin: 0; padding: 0; }
  html, body {
    width: 1200px; height: 934px; overflow: hidden;
    background: var(--backdrop);
    font-family: "Montserrat", sans-serif;
  }
  .sheet {
    width: 1200px; height: 934px;
    display: flex; align-items: center; justify-content: center; gap: 44px;
  }
  .card {
    position: relative; width: 520px; height: 297px; overflow: hidden;
    box-shadow: 0 10px 28px rgba(0,0,0,.14);
  }
  .card--back { background: var(--card-dark); color: var(--ink-light); }
  .card--front { background: var(--card-light); color: var(--ink-dark); }

  .deco { position: absolute; border-radius: 50%; }
  .card--back .deco { width: 230px; height: 230px; left: -40px; bottom: -70px; background: var(--deco-on-dark); }
  .card--front .deco { width: 200px; height: 200px; right: -70px; top: 90px; background: var(--deco-on-light); }

  .wordmark {
    position: absolute; top: 38px; right: 34px;
    display: flex; align-items: center; gap: 10px;
    font-weight: 700; font-size: 27px; letter-spacing: .5px;
  }
  .wordmark__dot { width: 20px; height: 20px; border-radius: 50%; background: var(--accent); }
  .card--back .wordmark__name { color: var(--ink-light); }
  .card--front .wordmark__name { color: var(--ink-dark); }

  .web {
    position: absolute; right: 34px; top: 168px; text-align: right;
    font-size: 13px; line-height: 1.9;
  }
  .web__accent { color: var(--accent); font-weight: 600; }

  .contact { position: absolute; left: 34px; bottom: 30px; font-size: 11.5px; line-height: 1.5; }
  .contact__name { font-weight: 700; font-size: 17px; letter-spacing: .6px; text-transform: uppercase; line-height: 1.2; }
  .contact__title { font-size: 12px; margin-bottom: 14px; }
  .contact__label { color: var(--accent); font-weight: 700; margin-right: 3px; }
  .contact__lines { margin-bottom: 14px; }
</style>
</head>
<body>
<main class="sheet">
  <section class="card card--back" aria-label="Card back">
    <div class="deco" role="img" aria-label="Faint brand decoration"></div>
    <div class="wordmark"><span class="wordmark__name">Bramble Harbor</span><span class="wordmark__dot"></span></div>
    <div class="web">
      <p>www.<span class="web__accent">BrambleHarbor</span>.com</p>
      <p>Network: brambleharbor</p>
    </div>
  </section>

  <section class="card card--front" aria-label="Card front">
    <div class="deco" role="img" aria-label="Faint brand decoration"></div>
    <div class="wordmark"><span class="wordmark__name">Bramble Harbor</span><span class="wordmark__dot"></span></div>
    <div class="contact">
      <p class="contact__name">Owen Marchetti</p>
      <p class="contact__title">President &amp; CEO</p>
      <div class="contact__lines">
        <p><span class="contact__label">P</span>805.555.0142 &nbsp;<span class="contact__label">C</span>818.555.0187</p>
        <p><span class="contact__label">E</span>owenmarchetti@brambleharbor.com</p>
      </div>
      <address style="font-style:normal">
        <p>2210 Alder Crest Road, Suite 140</p>
        <p>Fairmont Hills, CA 90210</p>
      </address>
    </div>
  </section>
</main>
</body>
</html>
```